I would like a standard letter head document that is innovative and not 'typically' corporate.
I would like a BLACK panel of some sort so that the logo can be best showcased within that (as the logo has a black background).
I would like the three words 'dream', 'believe', 'achieve'
inscribed at the side (as per the example I uploaded). Its should be more like a watermark so only just visible.
I would like the K symbol as a water mark on the page (similar to the lion on the example I uploaded).
I would like the following details also included.
Megan Tollisford
Personal Training/Nutrition/Life Coaching
www.larkvelbrook.com.au
0491 570 156
Life Coaching

```html
<!DOCTYPE html>
<html lang="en">
<head>
<meta charset="utf-8">
<title>Larkvelbrook Stationery</title>
<link href="https://fonts.googleapis.com/css2?family=Montserrat:wght@400;700;800&display=swap" rel="stylesheet">
<style>
  :root {
    --ink: #141414;
    --teal: #11a4a6;
    --paper: #ffffff;
    --mist-light: #f3f3f3;
    --mist-dark: #b9b9b9;
    --watermark: #e4e4e4;
    --body-text: #333333;
  }
  * { margin: 0; padding: 0; box-sizing: border-box; }
  html, body { width: 1200px; height: 849px; overflow: hidden; }
  body {
    position: relative;
    font-family: "Montserrat", Arial, sans-serif;
    background: radial-gradient(ellipse 70% 60% at 55% 45%, var(--mist-light) 0%, #dcdcdc 60%, var(--mist-dark) 100%);
  }
  .base-bands { position: absolute; left: 0; top: 0; width: 1200px; height: 849px; }

  .sheet { position: absolute; background: var(--paper); overflow: hidden; box-shadow: 0 1px 3px rgba(0,0,0,0.15); }
  .sheet__shapes { position: absolute; inset: 0; width: 100%; height: 100%; }

  .letterhead { left: 134px; top: 42px; width: 469px; height: 661px; }
  .envelope { left: 545px; top: 252px; width: 511px; height: 245px; }

  .brand-name {
    position: absolute;
    color: var(--teal);
    font-weight: 800;
    letter-spacing: 0.5px;
    text-transform: uppercase;
  }
  .letterhead .brand-name { left: 26px; top: 46px; font-size: 24px; }
  .envelope .brand-name { left: 18px; top: 26px; font-size: 21px; }

  .contact { position: absolute; color: var(--ink); line-height: 1.15; }
  .contact__name { font-weight: 700; font-size: 9.5px; letter-spacing: 0.2px; }
  .contact__line { font-weight: 400; font-size: 6.3px; color: var(--body-text); }
  .letterhead .contact { left: 333px; top: 26px; }
  .envelope .contact { left: 44px; top: 184px; }

  .k-watermark {
    position: absolute;
    left: 108px; top: 150px; width: 220px; height: 500px;
    background: radial-gradient(ellipse at center, var(--watermark) 0%, rgba(228,228,228,0.35) 70%, rgba(255,255,255,0) 100%);
  }
  .k-mark {
    position: absolute;
    left: 10px; top: 133px; width: 28px; height: 95px;
    background: linear-gradient(180deg, var(--teal), #0d8587);
    opacity: 0.85;
    border-radius: 3px;
  }
  .footer-url {
    position: absolute; right: 26px; bottom: 10px;
    color: var(--paper); font-size: 6.5px; font-weight: 700;
  }
</style>
</head>
<body>
  <svg class="base-bands" viewBox="0 0 1200 849" aria-hidden="true">
    <polygon points="0,715 603,757 603,849 0,849" fill="var(--ink)"/>
    <polygon points="603,757 1200,727 1200,849 603,849" fill="var(--teal)"/>
  </svg>

  <section class="sheet letterhead">
    <svg class="sheet__shapes" viewBox="0 0 469 661" aria-hidden="true">
      <polygon points="0,0 469,0 469,57 0,129" fill="var(--ink)"/>
      <polygon points="323,0 469,0 469,57 337,77" fill="var(--teal)"/>
      <polygon points="0,661 469,618 469,661" fill="var(--ink)"/>
    </svg>
    <div class="brand-name">Larkvelbrook</div>
    <div class="contact">
      <div class="contact__name">Megan Tollisford</div>
      <div class="contact__line">PersonalTraining/Nutrition/LifeCoaching</div>
      <div class="contact__line">www.larkvelbrook.com.au</div>
      <div class="contact__line">0491570156</div>
    </div>
    <div class="k-watermark" role="img" aria-label="Faint grey watermark of the brand's K monogram with sparkles"></div>
    <div class="footer-url">www.larkvelbrook.com.au</div>
  </section>

  <section class="sheet envelope">
    <svg class="sheet__shapes" viewBox="0 0 511 245" aria-hidden="true">
      <polygon points="0,0 511,0 511,13 0,94" fill="var(--ink)"/>
      <polygon points="336,0 511,0 511,13 326,42" fill="var(--teal)"/>
    </svg>
    <div class="brand-name">Larkvelbrook</div>
    <div class="k-mark" role="img" aria-label="Small teal K monogram with sparkles"></div>
    <div class="contact">
      <div class="contact__name">Megan Tollisford</div>
      <div class="contact__line">PersonalTraining/Nutrition/LifeCoaching</div>
      <div class="contact__line">www.larkvelbrook.com.au</div>
      <div class="contact__line">0491570156</div>
    </div>
  </section>
</body>
</html>
```